Renata Quisby

Luxury And Style -

Black - White & Gold

Target Market(s)

Fashion

Industry/Entity Type

Fashion

Requirements
Must have
• High-End
Nice to have
• We will Print on Silk Paper

```html
<!DOCTYPE html>
<html lang="en">
<head>
<meta charset="utf-8">
<title>Renata Quisby Letterhead</title>
<link href="https://fonts.googleapis.com/css2?family=Poppins:wght@400;500&family=Open+Sans:wght@400&display=swap" rel="stylesheet">
<style>
  :root {
    --backdrop: #eceef1;
    --paper: #ffffff;
    --ink: #2b2b2b;
    --ink-soft: #5a5a5a;
    --gold: #d9a93a;
    --gold-light: #f1d27a;
    --label-gold: #e09a2c;
    --band-grey: #e7e7e7;
  }
  * { margin: 0; padding: 0; box-sizing: border-box; }
  html, body {
    width: 922px; height: 1200px; overflow: hidden;
    background: var(--backdrop);
  }
  .letterhead {
    position: absolute; left: 33px; top: 0;
    width: 855px; height: 1200px;
    background: var(--paper);
    font-family: "Poppins", sans-serif;
    color: var(--ink);
  }
  .decor { position: absolute; left: 0; top: 0; width: 855px; height: 1200px; }
  .brand-name {
    position: absolute; left: 63px; top: 138px;
    font-size: 20px; font-weight: 400; letter-spacing: 2.6px;
    text-transform: uppercase; color: var(--ink);
  }
  .sender { position: absolute; left: 78px; top: 300px; }
  .sender-name { font-size: 24px; font-weight: 500; line-height: 30px; }
  .sender-role { font-size: 11.5px; color: var(--ink-soft); margin-top: 2px; }
  .sender-contacts { list-style: none; margin-top: 18px; }
  .sender-contacts li {
    font-size: 14px; color: var(--ink-soft); line-height: 23.6px;
  }
  .sender-contacts .label {
    display: inline-block; width: 28px; color: var(--label-gold); font-weight: 500;
  }
  .letter-date {
    position: absolute; right: 77px; top: 434px;
    font-family: "Open Sans", sans-serif; font-size: 17.5px; color: var(--ink-soft);
  }
  .letter-body {
    position: absolute; left: 78px; top: 502px; width: 700px;
    font-size: 14.2px; line-height: 25px; color: var(--ink-soft);
    text-align: justify; hyphens: auto;
  }
  .letter-body p + p { margin-top: 27px; }
  .signature {
    position: absolute; left: 91px; top: 891px; width: 108px; height: 66px;
    background: linear-gradient(90deg, #f3f3f3, #e4e4e4);
  }
  .signatory {
    position: absolute; left: 78px; top: 970px;
    font-size: 16px; font-weight: 500;
  }
  .footer-contacts {
    position: absolute; right: 76px; top: 982px;
    list-style: none; text-align: right;
    font-size: 11.5px; color: var(--ink-soft);
  }
  .footer-contacts li {
    display: flex; justify-content: flex-end; align-items: center; gap: 6px;
    margin-bottom: 10px; line-height: 15px;
  }
  .footer-contacts .icon {
    width: 15px; height: 15px; background: var(--ink); flex: none;
    display: flex; align-items: center; justify-content: center;
  }
</style>
</head>
<body>
<main class="letterhead">
  <svg class="decor" viewBox="0 0 855 1200" aria-hidden="true">
    <defs>
      <linearGradient id="halftone-top" x1="1" y1="0" x2="0.3" y2="0.9">
        <stop offset="0" stop-color="#d9a93a" stop-opacity="0.75"/>
        <stop offset="1" stop-color="#f1d27a" stop-opacity="0"/>
      </linearGradient>
      <linearGradient id="halftone-bottom" x1="0" y1="1" x2="0.9" y2="0.1">
        <stop offset="0" stop-color="#d9a93a" stop-opacity="0.75"/>
        <stop offset="1" stop-color="#f1d27a" stop-opacity="0"/>
      </linearGradient>
    </defs>
    <g role="img" aria-label="Gold halftone dot pattern fading across the top right corner">
      <polygon points="495,0 855,0 855,420" fill="url(#halftone-top)"/>
    </g>
    <polygon points="611,0 855,0 855,145" fill="var(--band-grey)"/>
    <polygon points="744,0 855,0 855,54" fill="#f6f6f6"/>
    <line x1="611" y1="0" x2="855" y2="145" stroke="var(--gold)" stroke-width="2"/>
    <line x1="744" y1="0" x2="855" y2="54" stroke="var(--gold-light)" stroke-width="1.5"/>

    <g role="img" aria-label="Gold halftone dot pattern fading across the bottom left corner">
      <polygon points="0,975 0,1200 340,1200" fill="url(#halftone-bottom)"/>
    </g>
    <polygon points="0,1121 311,1200 0,1200" fill="var(--band-grey)"/>
    <polygon points="0,1176 171,1200 0,1200" fill="#f6f6f6"/>
    <line x1="0" y1="1121" x2="311" y2="1200" stroke="var(--gold)" stroke-width="2"/>
    <line x1="0" y1="1176" x2="171" y2="1200" stroke="var(--gold-light)" stroke-width="1.5"/>
  </svg>

  <div class="brand-name">Renata Quisby</div>

  <section class="sender">
    <h1 class="sender-name">Callum Fenwright</h1>
    <p class="sender-role">Chief Director</p>
    <ul class="sender-contacts">
      <li><span class="label">A :</span>2713 Larkmoor Avenue, Brenton, BV 40518</li>
      <li><span class="label">W :</span>www.quisbyhouse.com</li>
      <li><span class="label">P :</span>+00 987 654 32</li>
      <li><span class="label">M :</span>studio@quisbymail.com</li>
    </ul>
  </section>

  <p class="letter-date">12 December, 2025</p>

  <article class="letter-body">
    <p>Lorem ipsum dolor sit amet, consectetuer adipiscing elit, sed diam nonummy nibh euismod tincidunt ut laoreet dolore magna aliquam erat volutpat. Ut wisi enim ad minim veniam, quis nostrud exerci tation ullamcorper suscipit lobortis nisl ut aliquip ex ea commodo consequat. Duis autem vel eum iriure dolor in hendrerit in vulputate velit esse molestie consequat, vel illum dolore eu feugiat nulla facilisis at vero eros et accumsan et iusto odio dignissim qui blandit praesent luptatum zzril delenit augue duis dolore te feugait nulla facilisi.</p>
    <p>Lorem ipsum dolor sit amet, cons ectetuer adipiscing elit, sed diam nonummy nibh euismod tincidunt ut laoreet dolore magna aliquam erat volutpat. Ut wisi enim ad minim veniam, quis nostrud exerci tation ullamcorper suscipit lobortis nisl ut aliquip ex ea commodo consequat.Lorem ipsum dolor sit amet, consectetuer adipiscing elit, sed diam nonummy nibh euismod tincidunt ut laoreet dolore magna aliquam eratveniam. suscipit lobortis nisl ut aliquip ex ea commodo consequat.Lorem ipsum dolor sit amet, consectetuer adipiscing elit, sed diam nonummy nibh euismod tincidunt ut laoreet dolore magna aliquam eratveniam.</p>
  </article>

  <div class="signature" role="img" aria-label="Handwritten signature of the signatory"></div>
  <p class="signatory">Mr. Oren Halvik</p>

  <ul class="footer-contacts">
    <li><span>2713 Larkmoor Avenue<br>Brenton, BV 40518</span>
      <span class="icon"><svg width="9" height="11" viewBox="0 0 9 11"><path d="M4.5 0.5a3.6 3.6 0 0 0-3.6 3.6c0 2.7 3.6 6.4 3.6 6.4s3.6-3.7 3.6-6.4A3.6 3.6 0 0 0 4.5.5z" fill="#fff"/><circle cx="4.5" cy="4.1" r="1.3" fill="#2b2b2b"/></svg></span></li>
    <li><span>+00 987 654 32</span>
      <span class="icon"><svg width="10" height="10" viewBox="0 0 10 10"><path d="M2.2 0.8l1.6 2-0.9 1.1c0.6 1.3 1.6 2.3 2.9 2.9l1.1-0.9 2 1.6-0.8 1.6C5 9 1 5 0.8 2z" fill="#fff"/></svg></span></li>
    <li><span>studio@quisbymail.com</span>
      <span class="icon"><svg width="10" height="8" viewBox="0 0 10 8"><rect x="0.5" y="0.5" width="9" height="7" fill="#fff"/><path d="M0.5 0.8L5 4.4 9.5 0.8" stroke="#2b2b2b" fill="none"/></svg></span></li>
    <li><span>www.quisbyhouse.com</span>
      <span class="icon"><svg width="9" height="10" viewBox="0 0 9 10"><path d="M1 0.5v8l2.2-2 1.5 3.2 1.4-.6-1.5-3.2h3z" fill="#fff"/></svg></span></li>
  </ul>
</main>
</body>
</html>
```